High Tech Real Estate Startup needs a business card

We are developing an innovative real estate marketing product based around advanced search and virtual reality.

We talk to people, we need business cards.

Target Market(s)

The target market is technology professionals and realtors.

Contact Information for Business Card

The information to be included will include

Name
Title
Phone Number
E-mail Address
www.quelzo.com

It should use simple iconography for each one of those fields.

Font styles to use
Other font styles liked:
• Co, Jubilat, Avenir

Colors

Designer to choose colors to be used in the design.

Requirements
Must have
• Clean aesthetic,
• Good use of negative space.
• It should use our company logo, shown in the attached file. It is able to use the negative of that logo (coloured font and white background) and I have attached other acceptable accent colours in a swatch file.
Should not have
• Should not be too busy
• No extraneous text (slogans, tag lines etc)

```html
<!DOCTYPE html>
<html lang="en">
<head>
<meta charset="utf-8">
<title>Quelzo business card</title>
<link rel="stylesheet" href="https://fonts.googleapis.com/css2?family=Montserrat:wght@400;500;600&display=swap">
<style>
  :root {
    --page: #4a423c;
    --card-dark: #242424;
    --card-light: #ffffff;
    --teal: #17b8bd;
    --text-light: #ffffff;
    --text-dark: #222222;
  }
  * { margin: 0; padding: 0; box-sizing: border-box; }
  html, body { width: 1200px; height: 930px; overflow: hidden; }
  body {
    background: var(--page);
    font-family: "Montserrat", sans-serif;
    position: relative;
  }
  .card {
    position: absolute;
    width: 560px;
    height: 320px;
    border-radius: 16px;
    overflow: hidden;
  }
  .card-back {
    left: 60px;
    top: 80px;
    background: var(--card-dark);
  }
  .network-pattern {
    position: absolute;
    inset: 0;
    background: radial-gradient(ellipse at 65% 30%, rgba(255,255,255,0.07), rgba(255,255,255,0) 60%),
                radial-gradient(ellipse at 30% 70%, rgba(255,255,255,0.05), rgba(255,255,255,0) 55%);
  }
  .brand-name {
    position: absolute;
    font-weight: 500;
    color: var(--teal);
    letter-spacing: 2px;
    line-height: 1;
  }
  .card-back .brand-name {
    left: 50%;
    top: 50%;
    transform: translate(-50%, -50%);
    font-size: 66px;
  }
  .card-front {
    left: 580px;
    top: 530px;
    background: var(--card-light);
  }
  .front-waves { position: absolute; inset: 0; }
  .card-front .brand-name {
    left: 52px;
    top: 125px;
    font-size: 66px;
  }
  .holder {
    position: absolute;
    right: 30px;
    top: 34px;
    text-align: right;
  }
  .holder-name {
    color: var(--teal);
    font-weight: 500;
    font-size: 20px;
    letter-spacing: 0.5px;
    line-height: 24px;
  }
  .holder-title {
    color: var(--text-dark);
    font-size: 12px;
    line-height: 16px;
    margin-top: 2px;
  }
  .contact {
    position: absolute;
    right: 22px;
    top: 188px;
    color: var(--text-light);
    font-size: 12.5px;
    text-align: right;
    line-height: 20px;
  }
  .contact-line { display: flex; justify-content: flex-end; align-items: center; gap: 8px; }
  .contact-line svg { width: 11px; height: 11px; }
  .address { margin-top: 8px; padding-right: 19px; }
</style>
</head>
<body>

<section class="card card-back">
  <div class="network-pattern" role="img" aria-label="Faint grey network constellation pattern of connected dots and lines"></div>
  <span class="brand-name">QUELZO</span>
</section>

<section class="card card-front">
  <svg class="front-waves" viewBox="0 0 560 320" width="560" height="320" aria-hidden="true">
    <path d="M560,108 C475,110 430,150 395,200 C345,270 280,305 150,320 L560,320 Z" fill="var(--card-dark)"/>
    <path d="M540,120 C475,126 435,156 408,198 C360,272 300,305 215,316" fill="none" stroke="var(--card-light)" stroke-width="4"/>
    <path d="M0,258 C120,292 255,272 335,205 C280,268 150,292 0,272 Z" fill="var(--teal)"/>
  </svg>

  <span class="brand-name">QUELZO</span>

  <div class="holder">
    <div class="holder-name">DANIEL HARPER</div>
    <div class="holder-title">Director</div>
  </div>

  <div class="contact">
    <div class="contact-line">+1-555-014-2288
      <svg viewBox="0 0 12 12"><path d="M3,1 L5,3.5 L4,5 C4.8,6.6 5.6,7.4 7,8 L8.5,7 L11,9 L9.5,11 C5,10.5 1.5,7 1,2.5 Z" fill="var(--teal)"/></svg>
    </div>
    <div class="contact-line">info@quelzo.com
      <svg viewBox="0 0 12 12"><rect x="1" y="2.5" width="10" height="7" fill="none" stroke="var(--teal)" stroke-width="1.2"/><path d="M1,2.5 L6,6.5 L11,2.5" fill="none" stroke="var(--teal)" stroke-width="1.2"/></svg>
    </div>
    <div class="contact-line">www.quelzo.com
      <svg viewBox="0 0 12 12"><circle cx="6" cy="6" r="5" fill="none" stroke="var(--teal)" stroke-width="1.2"/><ellipse cx="6" cy="6" rx="2.2" ry="5" fill="none" stroke="var(--teal)" stroke-width="1"/><path d="M1,6 H11" stroke="var(--teal)" stroke-width="1"/></svg>
    </div>
    <div class="address">3716 Alder Creek Rd.<br>Franklin, TN 37064</div>
  </div>
</section>

</body>
</html>
```